Kettle Ledger Business Card design

We need a stand out business card design for Accounting practice based in Australia specialising in pubs, clubs and hotels. We help venues maximise margins, create time and manage cashflow. One club we have been working with for the last 6 months has increased revenue by 3% and margin by 5% in this time frame. We have a back office outsourced system that costs less than having a full time employee and also allows the venues the added benefit of:<br/>-using the office space to become a revenue generating opportunity. <br/>-a complete system to enhance governance, accountability and efficiency within their operation<br/>-52 weeks cover so no hassle to cover annual/sick .. leave<br/><br/>We would like to see designs that use the colours of our logo (green & blue).
Target Market(s)
Australian Pubs, Clubs & Hotels abookkeeping, accounting and tax services
Industry/Entity Type
Accountant
Contact Information for Business Card
Miriam Oakley CPA
Principal
Accountant Tax Agent
Miriam@KettleLedger-example.com.au
0418693142
www.kettleledger-example.com.au
Accounting / Payroll / Tax / SMSF / Technology
Colors
Designer to choose colors to be used in the design.
Look and feel
Each slider illustrates characteristics of the customer's brand and the style your logo design should communicate.

```html
<!DOCTYPE html>
<html lang="en">
<head>
<meta charset="utf-8">
<title>Kettle Ledger Business Card</title>
<link href="https://fonts.googleapis.com/css2?family=Poppins:wght@700&family=Rubik:wght@600&family=Roboto:wght@400&display=swap" rel="stylesheet">
<style>
  :root {
    --page-bg: #e9ecf0;
    --card-bg: #f6f8fa;
    --brand-blue: #3b4b8f;
    --band-blue-top: #3d4f93;
    --band-blue-bottom: #27337a;
    --brand-green: #2e6b45;
    --text-muted: #4f5a80;
    --icon-green: #3a6a4d;
  }
  html, body {
    margin: 0;
    padding: 0;
    width: 1200px;
    height: 900px;
    overflow: hidden;
    background: var(--page-bg);
  }
  .business-card {
    position: absolute;
    left: 120px;
    top: 176px;
    width: 960px;
    height: 548px;
    background: var(--card-bg);
    box-shadow: 0 10px 30px rgba(30, 40, 80, 0.15);
    overflow: hidden;
  }
  .brand-band {
    position: absolute;
    top: 0;
    right: 0;
    width: 306px;
    height: 100%;
    background: linear-gradient(180deg, var(--band-blue-top), var(--band-blue-bottom));
  }
  .brand-name {
    position: absolute;
    left: 61px;
    top: 62px;
    margin: 0;
    font-family: "Poppins", sans-serif;
    font-weight: 700;
    font-size: 66px;
    line-height: 1;
    letter-spacing: -1px;
    color: var(--brand-blue);
  }
  .person {
    position: absolute;
    left: 61px;
    top: 250px;
  }
  .person-name {
    margin: 0 0 6px;
    font-family: "Rubik", sans-serif;
    font-weight: 600;
    font-size: 28px;
    color: var(--brand-green);
  }
  .person-role {
    margin: 0;
    font-family: "Roboto", sans-serif;
    font-size: 22px;
    line-height: 30px;
    color: var(--text-muted);
  }
  .contact-list {
    position: absolute;
    left: 61px;
    top: 405px;
    margin: 0;
    padding: 0;
    list-style: none;
    font-family: "Roboto", sans-serif;
    font-size: 22px;
    color: var(--text-muted);
  }
  .contact-item {
    display: flex;
    align-items: center;
    height: 37px;
  }
  .contact-icon {
    width: 18px;
    height: 18px;
    margin-right: 17px;
    fill: none;
    stroke: var(--icon-green);
    stroke-width: 2;
  }
  .contact-icon.solid {
    fill: var(--icon-green);
    stroke: none;
  }
</style>
</head>
<body>
  <main class="business-card">
    <div class="brand-band"></div>

    <h1 class="brand-name">Kettle Ledger</h1>

    <section class="person">
      <h2 class="person-name">Miriam Oakley CPA</h2>
      <p class="person-role">Principal</p>
      <p class="person-role">Accountant Tax Agent</p>
    </section>

    <ul class="contact-list">
      <li class="contact-item">
        <svg class="contact-icon solid" viewBox="0 0 24 24" aria-hidden="true">
          <path d="M6.6 10.8a15.1 15.1 0 0 0 6.6 6.6l2.2-2.2a1 1 0 0 1 1-.25 11.4 11.4 0 0 0 3.6.57 1 1 0 0 1 1 1V20a1 1 0 0 1-1 1A17 17 0 0 1 3 4a1 1 0 0 1 1-1h3.5a1 1 0 0 1 1 1c0 1.25.2 2.45.57 3.57a1 1 0 0 1-.25 1z"/>
        </svg>
        <span>0418693142</span>
      </li>
      <li class="contact-item">
        <svg class="contact-icon" viewBox="0 0 24 24" aria-hidden="true">
          <rect x="3" y="5" width="18" height="14" rx="1.5"/>
          <path d="M3.5 6l8.5 7 8.5-7"/>
        </svg>
        <span>Miriam@KettleLedger-example.com.au</span>
      </li>
      <li class="contact-item">
        <svg class="contact-icon" viewBox="0 0 24 24" aria-hidden="true">
          <circle cx="12" cy="12" r="9"/>
          <path d="M3 12h18M12 3c3 3.2 3 14.8 0 18M12 3c-3 3.2-3 14.8 0 18"/>
        </svg>
        <span>www.kettleledger-example.com.au</span>
      </li>
    </ul>
  </main>
</body>
</html>
```